Funeral Services Site

We need a website for a Funeral Services company. The old website is: www.rouwcentrumkorvelaer.be We need the same structure and text.

Target Market(s)

Customers.

Coding

Coded - Design and coding required

Number of Pages Required

4 page

Font styles to use
Serif
Sans Serif
Script

```html
<!DOCTYPE html>
<html lang="en">
<head>
<meta charset="utf-8">
<title>Funeral home Korvelaer bvba</title>
<link href="https://fonts.googleapis.com/css2?family=Playfair+Display:wght@400;700&family=Roboto:wght@400;500;700&display=swap" rel="stylesheet">
<style>
:root{
  --ink:#1c1c1c;
  --text:#4a4a4a;
  --dark:#3d3d3d;
  --footer:#555555;
  --soft:#f3f1ee;
  --white:#ffffff;
  --line:#7a7a7a;
}
*{margin:0;padding:0;box-sizing:border-box}
html,body{width:1200px;height:3158px;overflow:hidden}
body{position:relative;background:var(--white);font-family:'Roboto',sans-serif;color:var(--text)}
.abs{position:absolute}
.serif{font-family:'Playfair Display',serif}

/* header */
.site-header{left:0;top:0;width:1200px;height:65px;background:var(--white);z-index:5}
.brand{left:88px;top:10px;display:flex;align-items:center;gap:10px}
.brand-dot{width:42px;height:42px;border-radius:50%;background:var(--ink)}
.brand-name{font-family:'Playfair Display',serif;font-weight:700;font-size:20px;line-height:19px;color:var(--ink)}
.brand-name small{font-size:11px}
.main-nav{right:86px;top:29px;display:flex;gap:30px;font-size:13px;font-weight:500;color:#333}
.lang{left:1137px;top:0;width:63px;height:65px;background:var(--dark);color:#fff;font-size:13px;padding:27px 0 0 19px}

/* hero */
.hero{left:0;top:65px;width:1200px;height:800px;background:linear-gradient(160deg,#3c3e3d 0%,#6b6a68 22%,#8c8b89 45%,#8a8987 70%,#3a3b3a 100%)}
.hero-cut{left:0;top:690px;width:1200px;height:180px}
.hero-title{left:88px;top:352px;font-family:'Playfair Display',serif;font-weight:700;font-size:52px;line-height:49px;color:#fff}
.hero-sub{left:90px;top:458px;font-family:'Playfair Display',serif;font-size:23px;color:#fff}
.btn{display:inline-block;height:40px;line-height:38px;font-size:14px;font-weight:500;text-align:center;text-transform:uppercase}
.btn-dark{background:var(--dark);color:#fff;border:1px solid var(--dark)}
.btn-outline-light{border:1px solid #fff;color:#fff}
.btn-outline-dark{border:1px solid var(--dark);color:var(--dark)}
.slide-arrow{width:31px;height:69px;background:rgba(60,60,60,.8);color:#fff;font-size:14px;text-align:center;line-height:69px}

/* about */
.about-band{left:0;top:858px;width:1200px;height:613px;background:var(--soft)}
.flowers-photo{left:0;top:835px;width:260px;height:300px;background:radial-gradient(ellipse at 30% 40%,#e6e2dc 0%,#b7b1a8 45%,rgba(243,241,238,0) 75%)}
.section-title{font-family:'Playfair Display',serif;font-weight:700;font-size:40px;line-height:40px;color:var(--ink)}
.intro-title{left:300px;top:930px;width:600px;text-align:center}
.candle-photo{left:163px;top:1087px;width:355px;height:445px;background:linear-gradient(180deg,#8b8b8b 0%,#5a5a58 45%,#4a3d33 75%,#2e241e 100%)}
.body-copy{font-size:15px;line-height:24px;color:var(--text)}
.about-text{left:587px;top:1196px;width:480px;text-align:justify}
.about-text p+p{margin-top:13px}

/* organization */
.org-title{left:157px;top:1630px}
.org-text{left:155px;top:1721px;width:446px;text-align:justify}
.org-right{left:643px;top:1645px;width:425px}
.org-list{list-style:none;margin-top:16px}
.org-list li{position:relative;padding-left:16px;margin-bottom:4px}
.org-list li::before{content:"›";position:absolute;left:0;top:-1px;color:#888;font-size:17px}

/* gallery */
.gallery{left:0;top:1932px;width:1200px;height:348px;display:flex}
.gallery div{flex:1}

/* cta */
.cta-photo{left:0;top:2304px;width:280px;height:490px;background:radial-gradient(ellipse at 30% 50%,#f2d9d0 0%,#e9e3da 45%,rgba(255,255,255,0) 78%)}
.cta-title{left:200px;top:2416px;width:800px;text-align:center}
.cta-sub{left:0;top:2502px;width:1200px;text-align:center;font-size:16px;color:var(--text)}

/* footer */
.footer-shape{left:0;top:2660px;width:1200px;height:498px}
.footer-brand{left:160px;top:2930px;display:flex;align-items:center;gap:12px;color:#fff;font-family:'Playfair Display',serif;font-weight:700;font-size:24px;line-height:26px}
.footer-brand span.dot{width:44px;height:44px;border-radius:50%;border:2px solid #fff}
.footer-head{font-size:18px;font-weight:700;color:#fff;text-transform:uppercase}
.footer-links{left:505px;top:2855px}
.footer-links ul{list-style:none;margin-top:12px}
.footer-links li{font-size:14px;color:#f1f1f1;line-height:32px}
.footer-contact{left:777px;top:2855px}
.contact-row{position:relative;padding-left:32px;margin-top:16px;color:#f1f1f1;font-size:14px;line-height:17px}
.contact-row b{font-family:'Playfair Display',serif;font-size:14px;display:block}
.contact-row svg{position:absolute;left:0;top:4px}
.footer-rule{left:88px;top:3107px;width:1024px;height:1px;background:#6d6d6d}
.copyright{left:0;top:3124px;width:1200px;text-align:center;font-size:14px;color:#f1f1f1}
.to-top{left:1129px;top:3090px;width:32px;height:32px;border-radius:50%;background:#fff}
</style>
</head>
<body>

<header class="site-header abs">
  <div class="brand abs"><span class="brand-dot"></span><div class="brand-name">Funeral home<br>Korvelaer <small>bvba</small></div></div>
  <nav class="main-nav abs"><span>HOME</span><span>ABOUT US</span><span>CONDOLE ONLINE</span><span>ORDER FLOWERS</span><span>CONTACT</span></nav>
  <div class="lang abs">EN ⌄</div>
</header>

<section class="hero abs" role="img" aria-label="Photograph of a bouquet of roses and white flowers lying on grey concrete"></section>
<svg class="hero-cut abs" width="1200" height="180" viewBox="0 0 1200 180"><polygon points="0,168 1200,5 1200,180 0,180" fill="#f3f1ee"/></svg>
<div class="slide-arrow abs" style="left:0;top:393px">‹</div>
<div class="slide-arrow abs" style="left:1169px;top:393px">›</div>
<h1 class="hero-title abs">Mourning center<br>Korvelaer bvba:</h1>
<p class="hero-sub abs">condolences online via the website</p>
<a class="btn btn-dark abs" style="left:88px;top:509px;width:139px">011 62 38 40</a>
<a class="btn btn-outline-light abs" style="left:233px;top:509px;width:137px">Contact us</a>
<svg class="abs" style="left:590px;top:711px" width="20" height="32" viewBox="0 0 20 32"><rect x="1.5" y="1.5" width="17" height="29" rx="8.5" fill="none" stroke="#333" stroke-width="2"/><line x1="10" y1="8" x2="10" y2="14" stroke="#333" stroke-width="2"/></svg>

<section class="about-band abs"></section>
<div class="flowers-photo abs" role="img" aria-label="Photograph of white carnations"></div>
<svg class="abs" style="left:577px;top:874px" width="46" height="46" viewBox="0 0 46 46"><path d="M8 40V20a15 15 0 0 1 30 0v20z" fill="#b5b5b5"/><rect x="3" y="40" width="40" height="5" fill="#b5b5b5"/><path d="M23 14v16M18 20h10" stroke="#fff" stroke-width="2.5"/></svg>
<h2 class="section-title intro-title abs">Mourning center Korvelaer, a complete service in mourning and farewell guidance</h2>
<div class="candle-photo abs" role="img" aria-label="Photograph of a white candle among dried leaves and red berries"></div>
<h2 class="section-title abs" style="left:588px;top:1144px">About Us</h2>
<div class="about-text body-copy abs">
  <p>Saying goodbye to a loved one is one of the toughest things in a lifetime. Funeral home Korvelaer in Vossem takes care of all the practical and administrative matters involved. So you can say goodbye in peace.</p>
  <p>Our people have a ruime experience in farewell guidance and stand for 24 hours at 24 hours for you. Our fully renovated funeral home is open to you and your acquaintances, so that you can greet your loved one at any time of the day.</p>
</div>

<h2 class="section-title org-title abs">Organization funeral<br>and worship</h2>
<p class="org-text body-copy abs">The organization of the funeral ceremony is a moment of reflection, where the personality of the deceased can be beautifully highlighted. Our team will assist you in this and select the most beautiful texts, songs and photos with you in order to arrive at an appropriate and worthy goodbye.</p>
<div class="org-right body-copy abs">
  <p style="text-align:justify">The funeral can take place in your parish church or our auditorium if you wish, which can accommodate a maximum of 100 guests. We can arrange the following for you:</p>
  <ul class="org-list">
    <li>Vigil the night before the funeral</li>
    <li>Prayer service with priest (if possible)</li>
    <li>Eucharistic celebration with priest (on Tuesday and Friday in the parishes of Vossem)</li>
  </ul>
</div>

<div class="gallery abs">
  <div role="img" aria-label="Photograph of a bridal-style bouquet of roses" style="background:linear-gradient(160deg,#c9a99e,#8a7d70 50%,#d9d4cc)"></div>
  <div role="img" aria-label="Photograph of red candles burning" style="background:linear-gradient(180deg,#2d2320,#7a2a22 50%,#3a2b22)"></div>
  <div role="img" aria-label="Photograph of an open book with a white rose" style="background:linear-gradient(160deg,#151515,#3b3b38 55%,#1a1d1e)"></div>
  <div role="img" aria-label="Photograph of a woman seen from behind holding white tulips" style="background:linear-gradient(170deg,#cfcfc8,#7b6e63 45%,#3e3f40)"></div>
  <div role="img" aria-label="Photograph of pink and white flowers on a wooden coffin" style="background:linear-gradient(160deg,#5a3c28,#b7a6a2 50%,#6b4b33)"></div>
</div>
<div class="slide-arrow abs" style="left:0;top:2075px">‹</div>
<div class="slide-arrow abs" style="left:1169px;top:2075px">›</div>

<div class="cta-photo abs" role="img" aria-label="Photograph of pale pink roses with small white blossoms"></div>
<h2 class="section-title cta-title abs">Do you have any Questions Or would you like to call in our Funeral Home?</h2>
<p class="cta-sub abs">Contact us we are here for you.</p>
<a class="btn btn-dark abs" style="left:460px;top:2540px;width:137px">011 62 38 40</a>
<a class="btn btn-outline-dark abs" style="left:603px;top:2540px;width:137px">Contact us</a>

<svg class="footer-shape abs" width="1200" height="498" viewBox="0 0 1200 498"><polygon points="0,130 1200,5 1200,498 0,498" fill="#555555"/></svg>
<div class="footer-brand abs"><span class="dot"></span><div>Funeral home<br>Korvelaer</div></div>
<div class="footer-links abs">
  <div class="footer-head">Useful links</div>
  <ul><li>Home</li><li>About us</li><li>Condole online</li><li>Order flowers</li><li>Contact</li></ul>
</div>
<div class="footer-contact abs">
  <div class="footer-head">Contact us</div>
  <div class="contact-row"><svg width="20" height="14" viewBox="0 0 20 14"><rect width="20" height="14" fill="#9a9a9a"/><path d="M0 0l10 8 10-8" fill="none" stroke="#555" stroke-width="1.5"/></svg><b>Email</b>info@rouwcentrumkorvelaer.example</div>
  <div class="contact-row"><svg width="18" height="18" viewBox="0 0 24 24"><path d="M6.6 10.8a15 15 0 0 0 6.6 6.6l2.2-2.2a1 1 0 0 1 1-.25 11 11 0 0 0 3.6.6 1 1 0 0 1 1 1V20a1 1 0 0 1-1 1A17 17 0 0 1 3 4a1 1 0 0 1 1-1h3.5a1 1 0 0 1 1 1 11 11 0 0 0 .6 3.6 1 1 0 0 1-.25 1z" fill="#9a9a9a"/></svg><b>24/24, 7 sur 7</b>011 62 38 40</div>
  <div class="contact-row"><svg width="16" height="22" viewBox="0 0 16 22"><path d="M8 0a8 8 0 0 0-8 8c0 6 8 14 8 14s8-8 8-14a8 8 0 0 0-8-8zm0 11a3 3 0 1 1 0-6 3 3 0 0 1 0 6z" fill="#9a9a9a"/></svg><b>Lindelaan 18</b>3790 Heerveld (Vossem)</div>
</div>
<div class="footer-rule abs"></div>
<p class="copyright abs">Copyright 2019 | All Right Reserved</p>
<div class="to-top abs"><svg width="32" height="32" viewBox="0 0 32 32"><path d="M12 18l4-4 4 4" fill="none" stroke="#555" stroke-width="1.5"/></svg></div>

</body>
</html>
```